Simple graphic for a book or slide presentation

We are looking for a style that suits the style of our book. It's title is Harbor. Keeping a calm course through stormy seas. There will be more line drawing/graphics in the book but how you design this image will create the style for all the other simple graphics in the book (once we decide what they are). So this one design will lead to a few more to match the style of this one. We'd like the shape of the overall graphic (i.e the arrows and words/bubbles) to be circular (not a rounded square as appears in the sample attached). Perhaps the words don't need to be in ovals or bound by anything at all; perhaps they do - let's see what you see. We'd like you to choose a font or offer many different fonts you think will capture the practical yet unconventional tone of the book. The book is teaching that managing risks in life is a life-skill that can be learned. The section of the book where this graphic will be placed is called "the power of language" - basically we are saying that thoughts, words and actions create our culture and our destiny. This insight comes from Torvel Pelloru's famous quote:
Carefully watch your thoughts, for they become your words.
Manage and watch your words, for they will become your actions.
Consider and judge your actions, for they have become your habits.
Acknowledge and watch your habits, for they shall become your values.
Understand and embrace your values, for they become your destiny.

Please change the text in the middle of the graphic to say: The Human Culture Cycle

```html
<!DOCTYPE html>
<html lang="en">
<head>
<meta charset="utf-8">
<title>The Human Culture Cycle</title>
<link href="https://fonts.googleapis.com/css2?family=Montserrat:wght@500;600&display=swap" rel="stylesheet">
<style>
  :root {
    --page: #ffffff;
    --ring-dark: #b9babc;
    --ring-light: #dcdcde;
    --disc-top: #fbfbfb;
    --disc-bottom: #ededee;
    --hub-halo: #e4e5e7;
    --arrow: #c5c5c7;
    --icon-tone: #d3d4d6;
    --ink: #3a3a3c;
  }
  html, body {
    margin: 0;
    padding: 0;
    width: 1200px;
    height: 1200px;
    overflow: hidden;
    background: var(--page);
  }
  .cycle-diagram {
    display: block;
    width: 1200px;
    height: 1200px;
  }
  .arrow-path {
    fill: none;
    stroke: var(--arrow);
    stroke-width: 7;
    stroke-linecap: round;
  }
  .arrow-head { fill: var(--arrow); }
  .node-ring { fill: url(#ringGradient); }
  .node-disc { fill: url(#discGradient); }
  .node-icon { fill: var(--icon-tone); }
  .node-label {
    font-family: "Montserrat", sans-serif;
    font-weight: 600;
    font-size: 30px;
    fill: var(--ink);
    text-anchor: middle;
  }
  .hub-halo { fill: var(--hub-halo); }
  .hub-disc { fill: url(#discGradient); }
  .hub-title {
    font-family: "Montserrat", sans-serif;
    font-weight: 500;
    font-size: 42px;
    fill: var(--ink);
    text-anchor: middle;
    letter-spacing: 1px;
  }
</style>
</head>
<body>
<svg class="cycle-diagram" viewBox="0 0 1200 1200" xmlns="http://www.w3.org/2000/svg">
  <defs>
    <linearGradient id="ringGradient" x1="0" y1="0" x2="0" y2="1">
      <stop offset="0" stop-color="var(--ring-light)"/>
      <stop offset="1" stop-color="var(--ring-dark)"/>
    </linearGradient>
    <linearGradient id="discGradient" x1="0" y1="0" x2="1" y2="1">
      <stop offset="0" stop-color="var(--disc-top)"/>
      <stop offset="1" stop-color="var(--disc-bottom)"/>
    </linearGradient>
    <filter id="hubShadow" x="-20%" y="-20%" width="140%" height="140%">
      <feDropShadow dx="8" dy="10" stdDeviation="8" flood-color="#000" flood-opacity="0.12"/>
    </filter>
    <marker id="arrowTip" viewBox="0 0 28 26" refX="7" refY="13" markerWidth="28" markerHeight="26" markerUnits="userSpaceOnUse" orient="auto">
      <path class="arrow-head" d="M0,0 L28,13 L0,26 L7,13 Z"/>
    </marker>
  </defs>

  <!-- connecting arrows -->
  <g class="cycle-arrows">
    <path class="arrow-path" marker-end="url(#arrowTip)" d="M737.1,213.5 A412 412 0 0 1 851.0,274.0"/>
    <path class="arrow-path" marker-end="url(#arrowTip)" d="M1007.4,524.4 A412 412 0 0 1 1011.9,653.2"/>
    <path class="arrow-path" marker-end="url(#arrowTip)" d="M873.3,913.9 A412 412 0 0 1 764.0,982.2"/>
    <path class="arrow-path" marker-end="url(#arrowTip)" d="M468.9,992.5 A412 412 0 0 1 355.0,932.0"/>
    <path class="arrow-path" marker-end="url(#arrowTip)" d="M198.6,681.6 A412 412 0 0 1 194.1,552.8"/>
    <path class="arrow-path" marker-end="url(#arrowTip)" d="M332.7,292.1 A412 412 0 0 1 442.0,223.8"/>
  </g>

  <!-- central hub -->
  <g class="hub">
    <circle class="hub-halo" cx="603" cy="603" r="203"/>
    <circle class="hub-disc" cx="603" cy="603" r="175" filter="url(#hubShadow)"/>
    <text class="hub-title" x="603" y="535">The</text>
    <text class="hub-title" x="603" y="591">Human</text>
    <text class="hub-title" x="603" y="647">Culture</text>
    <text class="hub-title" x="603" y="703">Cycle</text>
  </g>

  <!-- stage nodes -->
  <g class="stage-node" transform="translate(603 191)">
    <circle class="node-ring" r="130"/>
    <circle class="node-disc" r="114"/>
    <rect class="node-icon" x="-70" y="-92" width="140" height="100" rx="14" role="img" aria-label="Icon: head in profile with a thought cloud"/>
    <text class="node-label" y="57">Thoughts</text>
  </g>

  <g class="stage-node" transform="translate(961 397)">
    <circle class="node-ring" r="130"/>
    <circle class="node-disc" r="114"/>
    <rect class="node-icon" x="-70" y="-92" width="140" height="100" rx="14" role="img" aria-label="Icon: head in profile with a speech bubble"/>
    <text class="node-label" y="55">Words</text>
  </g>

  <g class="stage-node" transform="translate(961 809)">
    <circle class="node-ring" r="130"/>
    <circle class="node-disc" r="114"/>
    <rect class="node-icon" x="-45" y="-100" width="90" height="120" rx="14" role="img" aria-label="Icon: pointing hand pressing a button"/>
    <text class="node-label" y="59">Actions</text>
  </g>

  <g class="stage-node" transform="translate(603 1016)">
    <circle class="node-ring" r="130"/>
    <circle class="node-disc" r="114"/>
    <rect class="node-icon" x="-52" y="-88" width="104" height="120" rx="14" role="img" aria-label="Icon: head in profile with gears inside"/>
    <text class="node-label" y="68">Habits</text>
  </g>

  <g class="stage-node" transform="translate(247 809)">
    <circle class="node-ring" r="130"/>
    <circle class="node-disc" r="114"/>
    <rect class="node-icon" x="-55" y="-72" width="110" height="100" rx="14" role="img" aria-label="Icon: two open hands holding a heart"/>
    <text class="node-label" y="59">Values</text>
  </g>

  <g class="stage-node" transform="translate(247 397)">
    <circle class="node-ring" r="130"/>
    <circle class="node-disc" r="114"/>
    <rect class="node-icon" x="-62" y="-62" width="124" height="74" rx="14" role="img" aria-label="Icon: two people beside a globe"/>
    <text class="node-label" y="53">Culture</text>
  </g>
</svg>
</body>
</html>
```